Veterinarian specialized in Equine (horse) sports medicine needs logo and stationary design!

New veterinary clinic only focused on horses needs logo and stationary designs. The clinic works with sport horses including jumping horses, dressage horses and polo horses (all disciplines you can find online. No racing horses). Name of clinic is StrideCare and is based in Mexico City where there is a large and elite clientele of sports horses. My main focus is orthopedics and rehabilitation.
I think logo should include horse(s), especially if they are performing a sport (like jumping, etc).

Target Market(s)

Elite horse-owners of sport horses.

Industry/Entity Type

Horseback Riding

Requirements
Must have
• Great Logo! I like bold and bright colors (no pastels), but with a professional tone.

```html
<!DOCTYPE html>
<html lang="en">
<head>
<meta charset="utf-8">
<title>StrideCare Stationery</title>
<link href="https://fonts.googleapis.com/css2?family=Open+Sans:wght@400;600;700&display=swap" rel="stylesheet">
<style>
:root{
  --navy:#13205c;
  --teal:#15a8ad;
  --ink:#2b2b2b;
  --paper:#ffffff;
  --backdrop:#dfeded;
  --muted:#5a5a5a;
}
*{box-sizing:border-box;margin:0;padding:0}
html,body{width:1088px;height:1200px;overflow:hidden}
body{background:var(--backdrop);font-family:"Open Sans",sans-serif;color:var(--ink);position:relative}
.piece{position:absolute;background:var(--paper)}
.brand{display:flex;align-items:center;gap:7px;font-family:"Open Sans",sans-serif;font-weight:600;color:var(--navy);letter-spacing:-.01em;white-space:nowrap}
.brand-square{background:var(--teal);flex:none}

/* business card front */
.card-front{left:92px;top:283px;width:274px;height:168px;background:var(--navy);display:flex;align-items:center;justify-content:center}
.card-front .brand{color:#fff;font-size:27px}
.card-front .brand-square{width:22px;height:22px}

/* business card back */
.card-back{left:92px;top:532px;width:274px;height:168px}
.card-back .brand{position:absolute;left:30px;top:30px;font-size:15px}
.card-back .brand-square{width:12px;height:12px}
.contact{position:absolute;left:171px;top:56px;line-height:1.25}
.contact-name{color:var(--teal);font-size:12px}
.contact-role{color:var(--navy);font-size:8.5px;font-weight:600;margin-bottom:6px}
.contact-phone{color:var(--navy);font-size:8.5px;font-weight:600}
.contact-mail{color:var(--muted);font-size:6.5px;margin-bottom:8px}
.contact-addr{color:var(--muted);font-size:6.5px;line-height:1.4}

/* letterhead */
.letterhead{left:463px;top:69px;width:542px;height:767px}
.letterhead .brand{position:absolute;left:118px;top:80px;font-size:23px}
.letterhead .brand-square{width:18px;height:18px}
.salutation{position:absolute;left:118px;top:178px;font-size:13.5px;color:var(--ink)}
.letter-body{position:absolute;left:118px;top:236px;width:317px;font-size:9.8px;line-height:16.3px;text-align:justify;color:var(--ink)}
.letter-body p{margin-bottom:16.3px}
.closing{position:absolute;right:107px;top:528px;text-align:right;font-size:9.8px;line-height:16.3px}
.signature{position:absolute;left:320px;top:562px;width:118px;height:70px;background:#eef0f3;border-radius:4px}
.letter-footer{position:absolute;left:0;bottom:0;width:100%;height:77px;background:var(--navy);color:#fff;font-size:9.8px;display:flex;align-items:center;justify-content:center}

/* envelope */
.envelope{left:440px;top:880px;width:585px;height:254px}
.envelope .brand{position:absolute;right:52px;top:54px;font-size:19px}
.envelope .brand-square{width:15px;height:15px}
.env-window{position:absolute;left:48px;top:114px;width:218px;height:98px;border:1px solid #dcdcdc;border-radius:9px;background:#f2f2f2}
</style>
</head>
<body>

<section class="piece card-front" aria-label="Business card front">
  <div class="brand"><span class="brand-square"></span>StrideCare</div>
</section>

<section class="piece card-back" aria-label="Business card back">
  <div class="brand"><span class="brand-square"></span>StrideCare</div>
  <div class="contact">
    <div class="contact-name">Marco Ruiz</div>
    <div class="contact-role">Equine Vet</div>
    <div class="contact-phone">+ 52 55 4821 7730</div>
    <div class="contact-mail">marco@stridecare.mx</div>
    <div class="contact-addr">48 Calle Roble Norte<br>Lomas de Chapultepec<br>Mexico</div>
  </div>
</section>

<section class="piece letterhead" aria-label="Letterhead">
  <div class="brand"><span class="brand-square"></span>StrideCare</div>
  <p class="salutation">Dear Mr. Alvarez,</p>
  <div class="letter-body">
    <p>Lorem ipsum dolor sit amet, consectetur adipiscing elit. Donec orci purus, luctus vitae dignissim eu, iaculis sed purus. Vivamus faucibus, ipsum nec aliquet viverra, leo mauris condimentum ligula, sit amet sagittis enim ligula quis arcu. Nam egestas tortor id nisi porttitor mattis. In tortor ante, ultricies in suscipit a, tempus non massa. Vivamus et auctor mi. Fusce vel massa nulla.</p>
    <p>Donec malesuada orci vitae nulla accumsan porta a id massa. Quisque accumsan iaculis magna sit amet fringilla. Maecenas consequat, magna eget tincidunt semper, odio nibh rutrum mi, id feugiat ante nisi eu risus.</p>
    <p>Duis aute irure dolor in reprehenderit in voluptate velit esse cillum dolore eu fugiat nulla pariatur. Excepteur sint occaecat cupidatat non proident, sunt in culpa qui officia deserunt mollit anim id est laborum. Sed ut perspiciatis unde omnis iste natus error sit voluptatem accusantium doloremque laudantium.</p>
  </div>
  <div class="closing">Sincerily,<br>Tomás Valdivia</div>
  <div class="signature" role="img" aria-label="Handwritten signature of Tomás Valdivia"></div>
  <footer class="letter-footer">210 Paseo Arboleda, Miguel Hidalgo, CDMX 11000, hola@stridecare.mx, +52 55 1234 5678</footer>
</section>

<section class="piece envelope" aria-label="Window envelope">
  <div class="env-window"></div>
  <div class="brand"><span class="brand-square"></span>StrideCare</div>
</section>

</body>
</html>
```